Graphic Design of Business Process

We require an eye-catching, sophisticated design of 2 business processes (attached), that will be used digitally AND for print (to be put on walls in our office).

The basic layout is attached. We require a creative, professional designer to re-design these so that they look appealing but still able to grasp all the information.

We will require vector files and editable project files for final delivery. You may refer to our website (kitefieldmedia.com.au) for an indication of our brand.

If you have any questions, please ask.

Thank you.

```html
<!DOCTYPE html>
<html lang="en">
<head>
<meta charset="utf-8">
<title>Sales to Content Funnel</title>
<link rel="stylesheet" href="https://fonts.googleapis.com/css2?family=Didact+Gothic&family=PT+Sans:wght@400;700&display=swap">
<style>
  :root {
    --ink: #000000;
    --band: #3a3a3a;
    --accent: #f2e000;
    --paper: #ffffff;
    --tier-light: #f5f07c;
    --tier-deep: #e0d800;
    --tier-title: #ffffff;
    --tier-text: #111111;
  }
  html, body {
    margin: 0;
    padding: 0;
    overflow: hidden;
    background: var(--paper);
  }
  .canvas {
    position: relative;
    width: 1200px;
    height: 1200px;
    overflow: hidden;
    background: var(--paper);
    font-family: "Didact Gothic", "Century Gothic", sans-serif;
  }
  .funnel-title {
    position: absolute;
    left: 252px;
    top: 30px;
    width: 668px;
    margin: 0;
    font-family: "Didact Gothic", sans-serif;
    font-weight: 400;
    font-size: 45px;
    letter-spacing: 1px;
    color: var(--ink);
    white-space: nowrap;
    text-align: center;
    border-bottom: 4px solid var(--ink);
    line-height: 50px;
  }
  .funnel {
    position: absolute;
    left: 0;
    top: 0;
  }
  .stage-name { fill: var(--accent); font-size: 18px; }
  .stage-task { fill: var(--paper); font-size: 10px; }
  .stage-note { fill: var(--accent); font-size: 7.5px; }
  .tag-box { fill: var(--paper); stroke: var(--accent); stroke-width: 2; }
  .tag-head { fill: var(--ink); font-size: 8.5px; }
  .tag-sub { fill: #333; font-size: 8px; }
  .flow { fill: none; stroke: var(--ink); stroke-width: 2; }
  .hierarchy-title {
    position: absolute;
    left: 0;
    top: 592px;
    width: 1164px;
    margin: 0;
    text-align: center;
    font-family: "PT Sans", sans-serif;
    font-weight: 700;
    font-size: 46px;
    color: var(--ink);
    line-height: 56px;
  }
  .tiers {
    position: absolute;
    left: 418px;
    top: 674px;
    width: 316px;
    height: 480px;
    border: 5px solid var(--ink);
    display: flex;
    flex-direction: column;
    background: linear-gradient(90deg, var(--tier-light), var(--tier-deep));
    font-family: "PT Sans", sans-serif;
  }
  .tier {
    flex: 1;
    display: flex;
    flex-direction: column;
    align-items: center;
    justify-content: center;
    text-align: center;
  }
  .tier + .tier { border-top: 3px solid var(--ink); }
  .tier-hero { flex: 0 0 161px; }
  .tier-hub { flex: 0 0 159px; }
  .tier-name {
    margin: 0;
    font-size: 33px;
    font-weight: 700;
    color: var(--tier-title);
    line-height: 38px;
  }
  .tier-role {
    margin: 4px 0 0;
    font-size: 19px;
    font-weight: 700;
    color: var(--tier-text);
    line-height: 24px;
    white-space: nowrap;
  }
</style>
</head>
<body>
<div class="canvas">
  <h1 class="funnel-title">SALES —› CONTENT FUNNEL</h1>

  <svg class="funnel" width="1200" height="600" viewBox="0 0 1200 600" aria-label="Sales funnel with awareness, consideration and action stages">
    <defs>
      <marker id="arrowhead" viewBox="0 0 10 10" refX="8" refY="5" markerWidth="6" markerHeight="6" orient="auto-start-reverse">
        <path d="M0,0 L10,5 L0,10 z" fill="#000"/>
      </marker>
    </defs>

    <g class="stage stage-awareness">
      <polygon points="248,140 912,140 836,248 324,248" fill="var(--ink)"/>
      <polygon points="324,248 808,248 820,266 336,266" fill="var(--band)"/>
      <text class="stage-name" x="314" y="181">AWARENESS</text>
      <text class="stage-task" x="330" y="194">IDENTIFY PROBLEM/NEED</text>
      <text class="stage-note" x="332" y="206">- ASPIRATIONAL</text>
      <text class="stage-note" x="332" y="216">- MARKET THE <tspan text-decoration="underline">OUTCOME</tspan> NOT PRODUCT</text>
    </g>

    <g class="stage stage-consideration">
      <polygon points="336,266 820,266 732,374 408,374" fill="var(--ink)"/>
      <polygon points="424,374 712,374 724,392 436,392" fill="var(--band)"/>
      <text class="stage-name" x="404" y="305">CONSIDERATION</text>
      <text class="stage-task" x="416" y="318">EVALUATE ALTERNATIVES</text>
      <text class="stage-note" x="418" y="331">- WHY IS <tspan text-decoration="underline">THIS SOLUTION</tspan> BETTER THAN OTHERS</text>
      <text class="stage-note" x="418" y="341">- <tspan text-decoration="underline">HOW</tspan> IS THIS PROVIDER GOING TO SOLVE MY NEED</text>
    </g>

    <g class="stage stage-action">
      <polygon points="436,392 724,392 582,550" fill="var(--ink)"/>
      <text class="stage-name" x="490" y="425">ACTION/DECISION</text>
      <text class="stage-task" x="502" y="437">PRESENT AN OFFER</text>
      <text class="stage-note" x="504" y="449">- <tspan text-decoration="underline">WHICH</tspan> PROVIDER ?</text>
    </g>

    <g class="flows">
      <path class="flow" d="M586,551 Q640,546 686,530" marker-start="url(#arrowhead)"/>
      <path class="flow" d="M744,496 C810,450 830,390 790,333" marker-end="url(#arrowhead)"/>
      <path class="flow" d="M744,496 C840,430 930,330 877,203" marker-end="url(#arrowhead)"/>
    </g>

    <g class="tag tag-problem">
      <rect class="tag-box" x="742" y="166" width="196" height="37"/>
      <text class="tag-head" x="747" y="181">PROBLEM &amp; SOLUTION</text>
      <text class="tag-sub" x="747" y="193">SUBJECT SHOWING SYMPTOMS OF PROBLEM</text>
    </g>
    <g class="tag tag-providers">
      <rect class="tag-box" x="674" y="298" width="166" height="36"/>
      <text class="tag-head" x="680" y="313">PROVIDERS &amp; TYPES OF SOLUTION</text>
      <text class="tag-sub" x="680" y="324">SUBJECT GIVES NAME TO PROBLEM</text>
    </g>
    <g class="tag tag-convert">
      <rect class="tag-box" x="616" y="446" width="104" height="32"/>
      <text class="tag-head" x="625" y="464">CONVERT &amp; RETAIN</text>
    </g>
    <g class="tag tag-referral" transform="translate(712,519) rotate(-35)">
      <rect class="tag-box" x="-36" y="-17" width="72" height="34"/>
      <text class="tag-head" x="0" y="-2" text-anchor="middle">WOM &amp;</text>
      <text class="tag-head" x="0" y="9" text-anchor="middle">REFERRAL</text>
    </g>
  </svg>

  <h2 class="hierarchy-title">CONTENT HIERARCHY</h2>

  <div class="tiers">
    <section class="tier tier-hero">
      <h3 class="tier-name">HERO</h3>
      <p class="tier-role">TENTPOLE CAMPAIGNS</p>
    </section>
    <section class="tier tier-hub">
      <h3 class="tier-name">HUB</h3>
      <p class="tier-role">REGULAR “PUSH” CONTENT</p>
    </section>
    <section class="tier tier-hygiene">
      <h3 class="tier-name">HYGIENE</h3>
      <p class="tier-role">ALWAYS-ON “PULL” CONTENT</p>
    </section>
  </div>
</div>
</body>
</html>
```